Tennis String Package

Need a design for a tennis string package.
Design to be 15 cm in length and width.
I would like to create a style like the one in the image.
Brand name VUMEX
Product name SKYBOUND
Front and back designs are required.

Colors
0054AA
0677BA
7BADD7
CADEEF
E8F1F8
A7469A
B969AE
D3A5CF
EDDBEB
F8F0F9
6B429C
8869AF
B7A5CE
E3DAEB
F3F0F8

```html
<!DOCTYPE html>
<html lang="en">
<head>
<meta charset="utf-8">
<title>VUMEX SKYBOUND – String Package</title>
<link rel="stylesheet" href="https://fonts.googleapis.com/css2?family=Poppins:wght@300;400;600&display=swap">
<style>
  :root {
    --page: #ffffff;
    --ink-muted: #6b6b6b;
    --text-light: #ffffff;
    --navy-deep: #262d4c;
    --navy: #213a69;
    --blue-mid: #2c5189;
    --blue-soft: #3a6193;
    --navy-dark: #1f2745;
    --slate: #566887;
    --slate-warm: #5f6278;
    --swatch-light: #e4e2c8;
    --swatch-dark: #9c9a80;
  }
  * { margin: 0; padding: 0; box-sizing: border-box; }
  html, body {
    width: 1200px; height: 800px; overflow: hidden;
    background: var(--page);
    font-family: "Poppins", sans-serif;
  }
  .canvas { position: relative; width: 1200px; height: 800px; }
  .size-note {
    position: absolute; left: 235px; top: 50px;
    font-weight: 300; font-size: 18px; color: var(--ink-muted);
  }
  .panel {
    position: absolute; top: 117px; width: 475px; height: 570px;
    overflow: hidden; color: var(--text-light);
    background:
      radial-gradient(ellipse 60% 20% at 60% 30%, rgba(80,125,180,.45), transparent 70%),
      radial-gradient(ellipse 70% 18% at 30% 80%, rgba(60,105,165,.4), transparent 70%),
      linear-gradient(150deg,
        var(--navy-deep) 0%, var(--navy) 18%, var(--blue-soft) 33%,
        var(--blue-mid) 45%, var(--navy-dark) 58%, var(--blue-mid) 70%,
        var(--navy-dark) 80%, var(--slate) 93%, var(--slate-warm) 100%);
  }
  .panel--front { left: 91px; }
  .panel--back { left: 641px; }

  .brand-name {
    position: absolute; font-weight: 600; font-size: 27px;
    letter-spacing: 1.5px; line-height: 1;
  }
  .product-name {
    position: absolute; font-weight: 400; font-size: 10.5px;
    letter-spacing: 5px; line-height: 1;
  }
  .small { font-size: 7.2px; font-weight: 400; line-height: 1; position: absolute; white-space: nowrap; }

  /* front */
  .panel--front .brand-name { left: 103px; top: 247px; }
  .panel--front .product-name { left: 301px; top: 252px; }
  .front-specs { position: absolute; left: 103px; top: 305px; font-size: 7.2px; line-height: 13px; }

  /* back */
  .panel--back .brand-name { left: 80px; top: 80px; }
  .panel--back .product-name { left: 320px; top: 86px; }
  .spec-row { position: absolute; left: 80px; top: 232px; width: 307px; height: 11px; border-bottom: 0.8px solid var(--text-light); }
  .spec-row .small { top: 1px; }
  .spec-divider { position: absolute; top: 0; width: 0.8px; height: 11px; background: var(--text-light); }
  .composition { position: absolute; left: 246px; top: 245px; font-size: 7.2px; line-height: 12.3px; }
  .description { position: absolute; left: 80px; top: 292px; font-size: 7.2px; line-height: 12.3px; }
  .string-swatch {
    position: absolute; left: 339px; top: 360px; width: 45px; height: 47px; border-radius: 2px;
    background: repeating-linear-gradient(90deg, var(--swatch-light) 0 3px, var(--swatch-dark) 3px 4.5px);
  }
  .recycle-icon { position: absolute; left: 152px; top: 424px; width: 17px; height: 17px; }
  .exclusive-note { left: 80px; top: 446px; font-size: 7px; }
  .maker { position: absolute; left: 188px; top: 426px; font-size: 7px; line-height: 9px; }
  .tear-strip { position: absolute; left: 0; top: 522px; width: 475px; height: 30px; }
  .open-label { position: absolute; left: 10px; top: 533px; font-size: 7px; }
</style>
</head>
<body>
<div class="canvas">
  <p class="size-note">15 cm x 18 cm</p>

  <section class="panel panel--front">
    <div class="brand-name">VUMEX</div>
    <div class="product-name">SKYBOUND</div>
    <div class="front-specs">
      <p>Tennis string made from 100% Polyester</p>
      <p>1.25mm</p>
      <p>16 L GA</p>
    </div>
  </section>

  <section class="panel panel--back">
    <div class="brand-name">VUMEX</div>
    <div class="product-name">SKYBOUND</div>

    <div class="spec-row">
      <span class="small" style="left:0">1.30mm / 16 GA</span>
      <span class="spec-divider" style="left:66px"></span>
      <span class="small" style="left:81px">12m/39ft</span>
      <span class="spec-divider" style="left:138px"></span>
      <span class="small" style="left:166px">Multifilament</span>
    </div>
    <div class="composition">
      <p>Composition: Nylon multifilament core</p>
      <p>with double winding nylon wraps</p>
    </div>
    <div class="description">
      <p>A comfortable and crisp string with optimal playability.</p>
      <p>For players of all swing speeds looking for a crisp response.</p>
    </div>

    <div class="string-swatch" role="img" aria-label="Close-up of the cream coloured string"></div>

    <svg class="recycle-icon" viewBox="0 0 24 24" fill="none" stroke="#fff" stroke-width="1.2" stroke-linejoin="round" role="img" aria-label="Recyclable">
      <path d="M10 4.5 L4.5 14"/>
      <path d="M14 4 L17.5 10"/>
      <path d="M16.5 7.6 L17.8 10.6 L14.6 10.4" fill="#fff"/>
      <path d="M20 14.5 L16.5 20.5 H11"/>
      <path d="M13 18.6 L10.6 20.5 L13 22.4" fill="#fff"/>
      <path d="M7 20.5 H3.5 L6.5 15"/>
      <path d="M4 16.4 L6.8 14.6 L8 17.8" fill="#fff"/>
    </svg>
    <span class="small exclusive-note">EXCLUSIVE USE FOR TENNIS</span>
    <div class="maker">
      <p>VUMEX,</p>
      <p>ADDRESS,</p>
      <p>www.vumexstrings.com</p>
    </div>

    <svg class="tear-strip" viewBox="0 0 475 30" fill="none" stroke="rgba(255,255,255,.75)" stroke-width="0.7">
      <path d="M12 0 Q0 15 12 30"/>
      <g>
        <path d="M14 6 L20 0 H32 M37 6 L43 0 H55 M60 6 L66 0 H78 M83 6 L89 0 H101 M106 6 L112 0 H124 M129 6 L135 0 H147 M152 6 L158 0 H170 M175 6 L181 0 H193 M198 6 L204 0 H216 M221 6 L227 0 H239 M244 6 L250 0 H262 M267 6 L273 0 H285 M290 6 L296 0 H308 M313 6 L319 0 H331 M336 6 L342 0 H354 M359 6 L365 0 H377 M382 6 L388 0 H400 M405 6 L411 0 H423 M428 6 L434 0 H446 M451 6 L457 0 H475"/>
        <path d="M27 24 L33 30 H45 M50 24 L56 30 H68 M73 24 L79 30 H91 M96 24 L102 30 H114 M119 24 L125 30 H137 M142 24 L148 30 H160 M165 24 L171 30 H183 M188 24 L194 30 H206 M211 24 L217 30 H229 M234 24 L240 30 H252 M257 24 L263 30 H275 M280 24 L286 30 H298 M303 24 L309 30 H321 M326 24 L332 30 H344 M349 24 L355 30 H367 M372 24 L378 30 H390 M395 24 L401 30 H413 M418 24 L424 30 H436 M441 24 L447 30 H459"/>
      </g>
    </svg>
    <span class="open-label">&#9654;OPEN</span>
  </section>
</div>
</body>
</html>
```